Heronby Mortgage Capital Business Card

We need a business card design for our mortgage servicing company. In addition to servicing the loans of homeowners, we help homeowners with purchasing their homes and any mortgage refinancing. We would like to see designs that use the colors in the logo attached below (gold-ish yellow and navy blue), and any other design you deem fit! The design should communicate a simpler life with smart mortgages provided by Heronby.

```html
<!DOCTYPE html>
<html lang="en">
<head>
<meta charset="utf-8">
<title>Heronby Mortgage Capital – Business Card</title>
<link rel="stylesheet" href="https://fonts.googleapis.com/css2?family=Arimo:wght@400;700&display=swap">
<style>
  :root {
    --backdrop: #c4c4c4;
    --paper: #ffffff;
    --navy: #262051;
    --gold: #e0ad2e;
    --ink-light: #ffffff;
    --shadow: rgba(0, 0, 0, 0.35);
  }
  * { box-sizing: border-box; margin: 0; padding: 0; }
  html, body {
    width: 1200px;
    height: 1015px;
    overflow: hidden;
    background: var(--backdrop);
    font-family: "Arimo", Arial, sans-serif;
  }
  .stage {
    position: relative;
    width: 1200px;
    height: 1015px;
  }
  .card {
    position: absolute;
    width: 700px;
    height: 400px;
    box-shadow: 6px 10px 18px var(--shadow);
  }
  .card__frame {
    position: absolute;
    inset: 28px;
    border: 2px solid var(--gold);
  }
  .card--front {
    left: 140px;
    top: 85px;
    background: var(--paper);
  }
  .card--back {
    left: 360px;
    top: 530px;
    background: var(--navy);
  }
  .brand {
    position: absolute;
    inset: 0;
    display: flex;
    align-items: center;
    justify-content: center;
  }
  .brand__name {
    font-weight: 700;
    font-size: 64px;
    color: var(--gold);
    letter-spacing: 0.5px;
  }
  .contact {
    position: absolute;
    inset: 0;
    display: flex;
    flex-direction: column;
    align-items: center;
    justify-content: center;
    text-align: center;
    color: var(--ink-light);
  }
  .contact__name {
    font-weight: 700;
    font-size: 26px;
    color: var(--gold);
    letter-spacing: 0.5px;
    line-height: 1.1;
  }
  .contact__role {
    font-size: 17px;
    letter-spacing: 0.5px;
    line-height: 1.3;
  }
  .contact__rule {
    width: 140px;
    height: 1px;
    background: var(--gold);
    margin: 18px 0;
  }
  .contact__lines {
    font-size: 20px;
    line-height: 1.25;
  }
</style>
</head>
<body>
  <main class="stage">
    <section class="card card--front" aria-label="Card front">
      <div class="card__frame"></div>
      <div class="brand">
        <span class="brand__name">Heronby Mortgage</span>
      </div>
    </section>

    <section class="card card--back" aria-label="Card back">
      <div class="card__frame"></div>
      <div class="contact">
        <p class="contact__name">DANIEL WHITFORD</p>
        <p class="contact__role">MANAGING DIRECTOR</p>
        <div class="contact__rule"></div>
        <p class="contact__lines">044-987 654 321<br>hello@heronby.com<br>www.heronbymortgage.com</p>
        <div class="contact__rule"></div>
        <p class="contact__lines">421 , Address line goes here<br>45452,Country Name</p>
      </div>
    </section>
  </main>
</body>
</html>
```